Startup Eyewear Store need Website

We are launching a new eyewear store. It's fun retro colors with bold wood tones. I will upload our logo to give you an idea of some fun colors. The site will need a cart and the ability to show multiple view of different eyewear frames. It will need standard buttons such as Contact Us, About Us, Blog, Social Media Feed, and New Releases, . The company will also have a Membership function and we need to be able to show that we can ship multiple frames have customers try them on and select which ones they want. We will need it responsive and all coding done.

Industry/Entity Type

Eyewear

Coding

Coded - Design and coding required

Number of Pages Required

1 page

Colors
f78f20

Requirements
Must have
• Clean Fund and Vintage Retro with some bright oranges.

```html
<!DOCTYPE html>
<html lang="en">
<head>
<meta charset="utf-8">
<title>Specs Parlour - Fashion Eyewear</title>
<link href="https://fonts.googleapis.com/css2?family=Lato:wght@400;700;900&display=swap" rel="stylesheet">
<style>
:root{
  --orange:#f78f20;
  --navy:#231a5c;
  --slate:#5d6b7a;
  --footer:#5f6b78;
  --yellow:#f5ec4a;
  --cyan:#1fc6dc;
  --grey:#efefef;
  --rule:#cfcfcf;
  --tile-border:#f06a6a;
  --text:#2b2b3a;
  --white:#ffffff;
}
*{box-sizing:border-box;margin:0;padding:0}
html,body{width:1200px;height:3169px;overflow:hidden;background:var(--white)}
body{font-family:'Lato',sans-serif;color:var(--text)}
.page{position:relative;width:1200px;height:3169px;overflow:hidden}

/* header */
.brand{position:absolute;left:100px;top:22px;display:flex;align-items:center;gap:12px}
.brand-dot{width:34px;height:34px;border-radius:50%;background:var(--orange)}
.brand-name{font-weight:900;font-size:30px;color:var(--orange)}
.contact{position:absolute;left:632px;top:42px;display:flex;gap:12px;align-items:center}
.contact-phone{font-weight:700;font-size:26px;color:var(--navy);line-height:1}
.contact-hours{font-weight:700;font-size:11px;color:var(--navy);margin-top:4px}
.divider{position:absolute;top:42px;width:2px;height:42px;background:var(--rule)}
.currency{position:absolute;left:938px;top:52px;font-weight:700;font-size:20px;color:var(--navy)}
.currency span{color:var(--orange);font-size:16px}
.cart{position:absolute;left:1052px;top:42px}

/* nav */
.nav{position:absolute;left:0;top:122px;width:1200px;height:55px;background:var(--slate)}
.nav ul{list-style:none;display:flex;gap:32px;position:absolute;left:100px;top:18px}
.nav li{font-weight:700;font-size:16px;color:var(--white)}
.nav li.active{color:var(--orange)}
.search{position:absolute;left:944px;top:17px;font-weight:700;font-size:17px;color:var(--white)}
.search-icon{position:absolute;left:1050px;top:10px}

/* hero */
.hero{position:absolute;left:0;top:177px;width:1200px;height:499px;background:var(--yellow);overflow:hidden}
.hero-photo{position:absolute;left:60px;top:0;width:540px;height:499px;background:linear-gradient(180deg,#f28ac6,#e8409a 55%,#6fa0c8)}
.hero-title{position:absolute;left:560px;top:130px;width:390px;text-align:center;font-weight:900;font-size:64px;letter-spacing:8px;line-height:74px;color:var(--navy)}
.hero-sub{position:absolute;left:560px;top:290px;width:390px;text-align:center;font-weight:900;font-size:23px;letter-spacing:1px;color:var(--navy)}
.btn-outline{position:absolute;border:3px solid var(--navy);color:var(--orange);font-weight:900;text-align:center}
.hero .btn-outline{left:687px;top:335px;width:126px;height:43px;line-height:37px;font-size:16px}
.vertical{position:absolute;font-weight:900;color:var(--navy);white-space:nowrap;transform-origin:left top}
.arrow-circle{position:absolute;width:40px;height:40px;border-radius:50%;border:3px solid var(--white)}

/* categories */
.tile-photo{position:absolute}
.cat-label{position:absolute;font-weight:900;font-size:40px;letter-spacing:8px;color:var(--navy);text-align:center}
.her-box{position:absolute;left:313px;top:697px;width:287px;height:279px;border:3px solid var(--tile-border)}
.her-box .cat-label{left:0;top:112px;width:100%}
.her-box .btn-outline{left:78px;top:180px;width:126px;height:40px;line-height:34px;font-size:15px}

/* products */
.section-title{position:absolute;left:0;width:1200px;text-align:center;font-weight:900;font-size:34px;letter-spacing:4px;color:var(--navy)}
.title-rule{position:absolute;left:560px;width:80px;height:3px;background:var(--orange)}
.tabs{position:absolute;left:0;width:1200px;display:flex;justify-content:center;gap:42px;font-size:26px;letter-spacing:1px;color:var(--navy)}
.tabs .on{color:var(--orange)}
.product{position:absolute;width:300px;text-align:center}
.product-img{margin:0 auto;width:220px;height:110px;border-radius:30px 30px 50px 50px}
.product-name{font-size:15px;letter-spacing:1px;color:var(--navy);margin-top:22px}
.product-price{font-size:16px;color:var(--navy);margin-top:6px}
.stars{color:var(--orange);font-size:13px;letter-spacing:2px;margin-top:8px}
.card{position:absolute;left:423px;top:1492px;width:348px;height:317px;background:var(--grey)}
.quick{position:absolute;right:0;top:0;width:144px;height:46px;background:var(--orange);color:var(--white);font-size:15px;font-weight:700;letter-spacing:1px;line-height:46px;text-align:center}
.add-cart{position:absolute;left:0;bottom:0;width:190px;height:50px;background:var(--orange);color:var(--white);font-size:15px;font-weight:700;letter-spacing:1px;display:flex;align-items:center;justify-content:center;gap:14px}
.slide-arrow{position:absolute;width:30px;height:30px}

/* promos */
.promo{position:absolute;top:2400px;height:271px;overflow:hidden}
.promo-photo{position:absolute;top:0;height:100%}
.promo h3{position:absolute;font-weight:900;font-size:25px;letter-spacing:7px;line-height:32px;text-align:center}
.promo p{position:absolute;font-size:13px;line-height:22px;text-align:center}

/* footer */
.footer{position:absolute;left:0;top:2768px;width:1200px;height:401px;background:var(--footer);color:var(--white)}
.footer-col{position:absolute;top:56px;list-style:none}
.footer-col li{font-weight:700;font-size:15px;letter-spacing:.5px;height:51px}
.footer-brand{position:absolute;left:104px;top:296px;display:flex;align-items:center;gap:12px}
.footer-copy{position:absolute;left:104px;top:364px;font-weight:700;font-size:14px}
.footer-hours{position:absolute;left:592px;top:325px;font-weight:700;font-size:16px}
.footer-phone{position:absolute;left:877px;top:318px;display:flex;gap:10px;align-items:center;font-weight:700;font-size:22px}
.social{position:absolute;left:877px;top:365px;display:flex;gap:10px}
.social span{width:20px;height:20px;background:var(--orange);border-radius:4px}
</style>
</head>
<body>
<div class="page">

  <header>
    <div class="brand"><span class="brand-dot"></span><span class="brand-name">Specs Parlour</span></div>
    <div class="contact">
      <svg width="36" height="36" viewBox="0 0 36 36"><circle cx="18" cy="18" r="16" fill="none" stroke="#f78f20" stroke-width="3"/><path d="M12 11c1-1 3-1 3 0l1 4-2 2c1 2 3 4 5 5l2-2 4 1c1 0 1 2 0 3-2 2-5 2-8 0-3-2-5-5-6-8 0-2 0-4 1-5z" fill="#f78f20"/></svg>
      <div><div class="contact-phone">(0100) 555 0199</div><div class="contact-hours">7 days a week 9:00am to 7:00pm</div></div>
    </div>
    <div class="divider" style="left:914px"></div>
    <div class="currency">USD <span>&#9660;</span></div>
    <div class="divider" style="left:1030px"></div>
    <svg class="cart" width="34" height="38" viewBox="0 0 34 38"><path d="M2 12h5l4 14h16l3-10H9" fill="none" stroke="#f78f20" stroke-width="2.5"/><circle cx="13" cy="31" r="2.5" fill="#f78f20"/><circle cx="25" cy="31" r="2.5" fill="#f78f20"/><circle cx="27" cy="6" r="6" fill="#f78f20"/><text x="27" y="9" font-size="8" fill="#fff" text-anchor="middle" font-family="Lato,sans-serif">0</text></svg>
  </header>

  <nav class="nav">
    <ul><li class="active">HOME</li><li>STORE</li><li>ABOUT US</li><li>BLOG</li><li>CONTACT US</li></ul>
    <div class="search">Search...</div>
    <svg class="search-icon" width="36" height="36" viewBox="0 0 36 36"><circle cx="15" cy="15" r="10" fill="none" stroke="#f78f20" stroke-width="3.5"/><path d="M22 22l10 10" stroke="#f78f20" stroke-width="4"/></svg>
  </nav>

  <section class="hero">
    <div class="hero-photo" role="img" aria-label="Model with bright pink hair wearing white round sunglasses"></div>
    <h1 class="hero-title">A WIDE<br>RANGE</h1>
    <div class="hero-sub">OF FASHION EYEWEAR</div>
    <div class="btn-outline">SHOP NOW!</div>
    <div class="vertical" style="left:12px;top:480px;transform:rotate(-90deg);font-size:28px;letter-spacing:3px;line-height:32px">NEW<br>COLLECTIONS</div>
    <div class="vertical" style="left:1120px;top:180px;transform:rotate(-90deg);font-size:28px;letter-spacing:3px;line-height:32px">FREE<br>SHIPPING</div>
    <div class="arrow-circle" style="left:10px;top:210px"><svg width="34" height="34"><path d="M20 9l-8 8 8 8" fill="none" stroke="#fff" stroke-width="3"/></svg></div>
    <div class="arrow-circle" style="left:1150px;top:210px"><svg width="34" height="34"><path d="M14 9l8 8-8 8" fill="none" stroke="#fff" stroke-width="3"/></svg></div>
  </section>

  <section class="categories">
    <div class="tile-photo" style="left:17px;top:697px;width:285px;height:279px;background:linear-gradient(135deg,#22d0d6,#f2e04a)" role="img" aria-label="Smiling model in yellow hat and sunglasses"></div>
    <div class="her-box"><div class="cat-label">HER</div><div class="btn-outline">SHOP NOW!</div></div>
    <div class="tile-photo" style="left:611px;top:697px;width:285px;height:279px;background:linear-gradient(135deg,#1d2fd8,#f5ec4a)" role="img" aria-label="Bearded man in mirrored sunglasses"></div>
    <div class="cat-label" style="left:960px;top:815px;width:180px">HIS</div>
    <div class="cat-label" style="left:20px;top:1125px;width:250px">TRENDY</div>
    <div class="tile-photo" style="left:302px;top:1006px;width:288px;height:279px;background:linear-gradient(135deg,#f5ec4a,#29a8e8)" role="img" aria-label="Model with blue hair in dark sunglasses"></div>
    <div class="cat-label" style="left:640px;top:1125px;width:200px">SALE</div>
    <div class="tile-photo" style="left:900px;top:1006px;width:287px;height:279px;background:linear-gradient(135deg,#22cfe0,#f04fa0)" role="img" aria-label="Laughing model in pink sunglasses"></div>
  </section>

  <section class="products">
    <h2 class="section-title" style="top:1345px">WOMEN</h2>
    <div class="title-rule" style="top:1392px"></div><div class="title-rule" style="top:1400px"></div>
    <div class="tabs" style="top:1428px"><span class="on">NEW</span><span>FEATURED</span><span>SPECIALS</span></div>
    <div class="card"><div class="quick">QUICK VIEW</div>
      <div class="add-cart">ADD TO CART <svg width="22" height="20" viewBox="0 0 22 20"><path d="M11 18S2 12 2 6.5A4.5 4.5 0 0 1 11 4a4.5 4.5 0 0 1 9 2.5C20 12 11 18 11 18z" fill="none" stroke="#fff" stroke-width="2"/></svg></div>
    </div>
    <div class="product" style="left:118px;top:1555px"><div class="product-img" role="img" aria-label="Matte black wrap sunglasses" style="background:linear-gradient(180deg,#3a3a3a,#c8c8c8)"></div><div class="product-name">MATTE-BLACK EYEWEAR</div><div class="product-price">$100.00</div></div>
    <div class="product" style="left:448px;top:1555px"><div class="product-img" role="img" aria-label="Cat-eye sunglasses with gold detail" style="background:linear-gradient(180deg,#2a2a2a,#9a8a7a)"></div><div class="product-name">CAT EYEWEAR</div><div class="product-price">$90.00 $100.00</div></div>
    <div class="product" style="left:790px;top:1555px"><div class="product-img" role="img" aria-label="Camo frame polarized sunglasses with blue lenses" style="background:linear-gradient(180deg,#6b5e4e,#1a62c8)"></div><div class="product-name">RIPTIDE POLARIZED EYEWEAR</div><div class="product-price">$80.00 $100.00</div><div class="stars">&#9733;&#9733;&#9733;&#9733;&#9733;</div></div>
    <svg class="slide-arrow" style="left:45px;top:1638px" viewBox="0 0 30 30"><circle cx="15" cy="15" r="13" fill="none" stroke="#f78f20" stroke-width="2"/><path d="M17 9l-6 6 6 6z" fill="#f78f20"/></svg>
    <svg class="slide-arrow" style="left:1132px;top:1638px" viewBox="0 0 30 30"><circle cx="15" cy="15" r="13" fill="none" stroke="#f78f20" stroke-width="2"/><path d="M13 9l6 6-6 6z" fill="#f78f20"/></svg>

    <h2 class="section-title" style="top:1852px">MEN</h2>
    <div class="title-rule" style="top:1899px"></div><div class="title-rule" style="top:1907px"></div>
    <div class="tabs" style="top:1935px"><span>NEW</span><span class="on">FEATURED</span><span>SPECIALS</span></div>
    <div class="product" style="left:118px;top:2050px"><div class="product-img" role="img" aria-label="Black square sunglasses with gold temple detail" style="background:linear-gradient(180deg,#111,#555);height:130px"></div><div class="product-name">DX 2016 EYEWEAR</div><div class="product-price">$60.00 $100.00</div><div class="stars">&#9733;&#9733;&#9733;&#9733;&#9733;</div></div>
    <div class="product" style="left:448px;top:2050px"><div class="product-img" role="img" aria-label="Rectangle sport frame with built-in earphones" style="background:linear-gradient(180deg,#1a1a1a,#6a6a6a);height:130px"></div><div class="product-name">RECTANGLE FRAME EYEWEAR</div><div class="product-price">$400.00 $500.00</div><div class="stars">&#9733;&#9733;&#9733;&#9733;&#9733;</div></div>
    <div class="product" style="left:790px;top:2050px"><div class="product-img" role="img" aria-label="Matte black wrap sunglasses" style="background:linear-gradient(180deg,#3a3a3a,#c8c8c8);height:130px"></div><div class="product-name">MATTE-BLACK EYEWEAR</div><div class="product-price">$100.00</div></div>
    <svg class="slide-arrow" style="left:45px;top:2135px" viewBox="0 0 30 30"><circle cx="15" cy="15" r="13" fill="none" stroke="#f78f20" stroke-width="2"/><path d="M17 9l-6 6 6 6z" fill="#f78f20"/></svg>
    <svg class="slide-arrow" style="left:1132px;top:2135px" viewBox="0 0 30 30"><circle cx="15" cy="15" r="13" fill="none" stroke="#f78f20" stroke-width="2"/><path d="M13 9l6 6-6 6z" fill="#f78f20"/></svg>
  </section>

  <section class="promo" style="left:27px;width:560px;background:var(--yellow)">
    <div class="promo-photo" style="left:0;width:210px;background:linear-gradient(135deg,#f3e9c8,#2a3a8c)" role="img" aria-label="Model with platinum hair in yellow sunglasses"></div>
    <h3 style="left:250px;top:45px;width:300px;color:var(--navy)">SHIPPING<br>AND DELIVERY</h3>
    <p style="left:255px;top:122px;width:290px;color:var(--navy)">Here you can read some details about a nifty little lifecycle of your order's journey from the time you place your order to your new treasures arriving at your doorstep.</p>
  </section>
  <section class="promo" style="left:611px;width:557px;background:linear-gradient(135deg,#1fb7e6,#1fd1e0)">
    <div class="promo-photo" style="left:0;width:200px;background:linear-gradient(180deg,#29b7e6,#f2ec3c 55%,#e6578c)" role="img" aria-label="Model in yellow top wearing pink sunglasses"></div>
    <h3 style="left:230px;top:45px;width:310px;color:var(--white)">PAYMENT<br>METHODS</h3>
    <p style="left:228px;top:122px;width:310px;color:var(--white)">It is equally important to choose the solution which offers a specific selection of credit cards that are most popular in the merchants target markets. We take all major cards as they are widely used by cyber customers.</p>
  </section>

  <footer class="footer">
    <ul class="footer-col" style="left:104px"><li>ABOUT</li><li>DELIVERY INFORMATION</li><li>PRIVACY POLICY</li><li>TERMS &amp; CONDITIONS</li></ul>
    <ul class="footer-col" style="left:429px"><li>CONTACT US</li><li>RETURNS</li><li>SITE MAP</li><li>BLOG</li></ul>
    <ul class="footer-col" style="left:680px"><li>BRANDS</li><li>GIFT CERTIFICATES</li><li>AFFILIATES</li><li>SPECIALS</li></ul>
    <ul class="footer-col" style="left:968px"><li>MY ACCOUNT</li><li>ORDER HISTORY</li><li>WISH LIST</li><li>NEWSLETTER</li></ul>
    <div class="footer-brand"><span class="brand-dot"></span><span class="brand-name">Specs Parlour</span></div>
    <div class="footer-copy">&copy; 2016 Specs Parlour.</div>
    <div class="footer-hours">7 days a week 9:00am to 7:00pm</div>
    <div class="footer-phone">
      <svg width="30" height="30" viewBox="0 0 36 36"><circle cx="18" cy="18" r="16" fill="none" stroke="#f78f20" stroke-width="3"/><path d="M12 11c1-1 3-1 3 0l1 4-2 2c1 2 3 4 5 5l2-2 4 1c1 0 1 2 0 3-2 2-5 2-8 0-3-2-5-5-6-8 0-2 0-4 1-5z" fill="#f78f20"/></svg>
      (0100) 555 0199
    </div>
    <div class="social"><span></span><span></span><span></span><span></span><span></span><span></span><span></span></div>
  </footer>
</div>
</body>
</html>
```